Need Bold, Hip Card for Concert Ticket Website Gleaming Passes!

Hi there! I am putting together a business/website that sells event tickets (mostly concerts, but also some sports and theater). Think SeatNook, but much smaller. The site is called Gleaming Passes. I have a new logo (attached, with black/red/white color scheme), and am looking for a modern/cool/original business card design. Note that I am thinking of having the card itself in the shape of a ticket (die cut), so you may want to keep that in mind when designing, but I'm not set on that. I'm also open to alternative card sizes, thicknesses, glossy, spot UV, etc. in order to stand out. I'm attaching a potential die cut template and a sample card using that template in case you want to work with that.
Target Market(s)
Music fans, people that like going to see live events
Industry/Entity Type
Entertainment
Contact Information for Business Card
Information that I'd like to have:
website address - www.gleamingpasses.example
phone number: 1-833-5GLEAMNG (532-6264)
my name - Wendel Pike

```html
<!DOCTYPE html>
<html lang="en">
<head>
<meta charset="utf-8">
<title>Gleaming Passes – Business Card</title>
<link rel="stylesheet" href="https://fonts.googleapis.com/css2?family=Montserrat:wght@800&family=Oswald:wght@500;600&display=swap">
<style>
  :root {
    --ticket-red: #9b0b0f;
    --ticket-red-dark: #7d080b;
    --ink: #161616;
    --paper: #ffffff;
    --backdrop: #ece7df;
  }
  html, body {
    margin: 0;
    width: 1200px;
    height: 800px;
    overflow: hidden;
    background: var(--backdrop);
  }
  .canvas {
    position: relative;
    width: 1200px;
    height: 800px;
  }
  .card {
    position: absolute;
    top: 252px;
    width: 520px;
    height: 297px;
    border-radius: 4px;
    box-shadow: 0 6px 18px rgba(0,0,0,0.18);
    overflow: hidden;
  }
  .card-back {
    left: 60px;
    background: var(--ticket-red);
  }
  .card-back .emblem-disc {
    position: absolute;
    left: 50%;
    top: 50%;
    width: 150px;
    height: 150px;
    margin: -75px 0 0 -75px;
    border-radius: 50%;
    background: var(--paper);
  }
  .card-front {
    left: 620px;
  }
  .card-front svg { display: block; }
  .brand-name {
    font-family: "Montserrat", sans-serif;
    font-weight: 800;
    fill: var(--ticket-red);
  }
  .holder-name {
    font-family: "Oswald", sans-serif;
    font-weight: 600;
    font-size: 46px;
  }
  .holder-first { fill: var(--ink); }
  .holder-last { fill: var(--ticket-red); }
  .web-address {
    font-family: "Oswald", sans-serif;
    font-weight: 600;
    font-size: 17px;
    fill: var(--ticket-red);
    letter-spacing: 0.5px;
  }
  .phone-line {
    font-family: "Oswald", sans-serif;
    font-weight: 500;
    font-size: 12px;
    fill: var(--ink);
    letter-spacing: 0.4px;
  }
</style>
</head>
<body>
<main class="canvas">
  <section class="card card-back" aria-label="Card back">
    <div class="emblem-disc"></div>
  </section>

  <section class="card card-front" aria-label="Card front">
    <svg width="520" height="297" viewBox="0 0 520 297" xmlns="http://www.w3.org/2000/svg">
      <rect class="frame" width="520" height="297" fill="var(--ticket-red)"/>
      <rect class="face" x="14" y="14" width="492" height="269" fill="var(--paper)"/>

      <!-- brand -->
      <circle cx="58" cy="68" r="26" fill="var(--ticket-red)"/>
      <text class="brand-name" x="96" y="62" font-size="36">GLEAMING</text>
      <text class="brand-name" x="98" y="98" font-size="24" letter-spacing="7">PASSES</text>

      <!-- divider -->
      <rect x="14" y="120" width="331" height="6" fill="var(--ticket-red)"/>
      <rect x="14" y="133" width="331" height="2" fill="var(--ticket-red)"/>

      <!-- holder -->
      <text class="holder-name" x="36" y="222"><tspan class="holder-first">WENDEL</tspan> <tspan class="holder-last">PIKE</tspan></text>

      <!-- stub separator -->
      <rect x="345" y="14" width="4" height="269" fill="var(--ticket-red)"/>

      <!-- contact stub -->
      <text class="web-address" transform="translate(378 272) rotate(-90)">WWW.GLEAMINGPASSES.EXAMPLE</text>
      <line x1="390" y1="22" x2="390" y2="276" stroke="var(--ticket-red)" stroke-width="1.5" stroke-dasharray="6 4"/>
      <text class="phone-line" transform="translate(410 272) rotate(-90)">1-833-5GLEAMNG (532-6264)</text>
      <rect x="419" y="14" width="14" height="269" fill="var(--ink)"/>

      <!-- tear stripes -->
      <g fill="var(--paper)">
        <rect x="437" y="20" width="60" height="5"/>
        <rect x="437" y="32" width="60" height="5"/>
        <rect x="437" y="44" width="60" height="5"/>
        <rect x="437" y="56" width="60" height="5"/>
        <rect x="437" y="68" width="60" height="5"/>
        <rect x="437" y="80" width="60" height="5"/>
        <rect x="437" y="92" width="60" height="5"/>
        <rect x="437" y="104" width="60" height="5"/>
        <rect x="437" y="116" width="60" height="5"/>
        <rect x="437" y="128" width="60" height="5"/>
        <rect x="437" y="140" width="60" height="5"/>
        <rect x="437" y="152" width="60" height="5"/>
        <rect x="437" y="164" width="60" height="5"/>
        <rect x="437" y="176" width="60" height="5"/>
        <rect x="437" y="188" width="60" height="5"/>
        <rect x="437" y="200" width="60" height="5"/>
        <rect x="437" y="212" width="60" height="5"/>
        <rect x="437" y="224" width="60" height="5"/>
        <rect x="437" y="236" width="60" height="5"/>
        <rect x="437" y="248" width="60" height="5"/>
        <rect x="437" y="260" width="60" height="5"/>
        <rect x="437" y="272" width="60" height="5"/>
      </g>
      <rect x="433" y="14" width="4" height="269" fill="var(--ticket-red)"/>
      <rect x="497" y="14" width="9" height="269" fill="var(--ticket-red)"/>
    </svg>
  </section>
</main>
</body>
</html>
```